Mobile App UI Redesign for Service Booking app

Bookora is a business management system made especially for service based businesses (our subscribers). It enables systemising your service businesses. This can be used by diverse industries like automotive service, beauty (hair salons, nail spas), Spas, Chiropractor, acupuntcure, osteo, yoga studio, business coach, etc.

One component of this management system is a consumer app that the users (customers of our subscribers) can use to book in services with businesses (subscribers). Any business that provides services, either 1-to-1(personal training/ hair cut, etc) or 1-to-many (classes/ sessions)can get their users to download the app and book straight away in real time.

The current app is built as a version that is available to all subscribers. Hence the search screen at the beginning of the app. Our subscribers have the option to brand this app, with their own logo and colours.

The UI of the app needs to be designed using flat and clean UI design trends that are currently prevailing for B2C apps. Even the sliding menu panel can be removed and alternative placement of this functionality can be suggested. The color palette used for the design should be limited (3-5 colours) so that minimum effort is required to convert this into our customers branded app.

The Current UI screens are open to suggestions for change. For ease of booking in minimum steps, consolidation of functionality on different screens can be suggested, accompanies by a rational reason with the objective of having a simple and straight forward user experience.

User should be able to move from one function to another (booking > view appointments > profile) in no more than 1 or max 2 gestures.

Target Market(s)

Service Based Businesses that require customers to book in services or sessions with them. These can include health services (chiro, physio, osteo, accupuncture, etc) Beauty (hair salon, nail spa, health spa, etc) automotive service (car service, motorcycle service, bike service, etc)

Industry/Entity Type

Business

Requirements
Must have
• Design files to be delivered in JPG and Vectored PSD format

```html
<!DOCTYPE html>
<html lang="en">
<head>
<meta charset="utf-8">
<title>Bookora — App Screens</title>
<link href="https://fonts.googleapis.com/css2?family=Open+Sans:wght@300;400;600;700&display=swap" rel="stylesheet">
<style>
  :root{
    --canvas:#ffffff;
    --accent:#f4b236;
    --purple:#b455c9;
    --navy:#2c3d51;
    --navy-line:#4b5b6e;
    --connect:#3f5aa0;
    --white:#ffffff;
    --ink:#222222;
    --muted:#dddddd;
  }
  *{box-sizing:border-box;margin:0;padding:0}
  html,body{width:683px;height:1200px;overflow:hidden;background:var(--canvas);font-family:"Open Sans",Arial,sans-serif}
  .board{position:relative;width:683px;height:1200px}
  .screen{position:absolute;width:330px;height:590px;overflow:hidden}
  .screen--signup{left:7px;top:6px}
  .screen--intro{left:346px;top:6px;background:var(--purple)}
  .screen--feed{left:7px;top:603px;background:var(--white)}
  .screen--menu{left:346px;top:603px;background:var(--navy)}

  .status{height:22px;display:flex;align-items:center;justify-content:space-between;padding:0 8px;font-size:9px;color:var(--white)}
  .status--dark{color:var(--ink)}
  .status__time{font-weight:600}
  .status__signal{display:flex;gap:2px;align-items:center}
  .status__signal i{width:4px;height:4px;border-radius:50%;background:currentColor;display:block}
  .status__battery{display:flex;align-items:center;gap:3px}
  .status__battery b{width:18px;height:8px;border:1px solid currentColor;border-radius:2px;display:block;position:relative}
  .status__battery b::after{content:"";position:absolute;inset:1px;background:currentColor}

  /* Sign up */
  .signup__photo{position:absolute;inset:0;background:linear-gradient(160deg,#7b7f86 0%,#51565f 45%,#3e3834 100%)}
  .signup__content{position:relative;height:100%}
  .brand{display:flex;align-items:center;justify-content:center;gap:8px;font-weight:300}
  .brand--hero{position:absolute;top:168px;left:0;right:0;color:var(--white);font-size:30px}
  .brand__dot{width:12px;height:12px;border-radius:50%;background:var(--accent);display:block}
  .form{position:absolute;top:300px;left:16px;right:16px;display:flex;flex-direction:column;gap:10px}
  .field{height:35px;border:1px solid rgba(255,255,255,.85);border-radius:4px;color:var(--white);font-size:11px;padding:0 10px;display:flex;align-items:center;background:rgba(0,0,0,.12)}
  .btn{height:35px;border-radius:18px;display:flex;align-items:center;justify-content:center;color:var(--white);font-size:11px;font-weight:600;letter-spacing:.3px;text-transform:uppercase}
  .btn--accent{background:var(--accent)}
  .btn--connect{background:var(--connect)}
  .form .btn--accent{margin-top:8px}
  .signin{text-align:center;color:var(--white);font-size:8px;margin-top:6px;line-height:1.5}
  .signin strong{display:block;color:var(--accent);font-size:9px;font-weight:600}

  /* Intro */
  .intro__orbit{position:absolute;left:62px;top:150px;width:206px;height:206px}
  .intro__title{position:absolute;left:0;right:0;top:242px;text-align:center;color:var(--white);font-size:22px;font-weight:400}
  .intro__tag{position:absolute;left:0;right:0;top:472px;text-align:center;color:var(--white);font-size:18px}
  .intro__dots{position:absolute;left:0;right:0;top:508px;display:flex;justify-content:center;gap:5px}
  .intro__dots i{width:5px;height:5px;border-radius:50%;background:rgba(255,255,255,.55);display:block}
  .intro__dots i.is-active{background:var(--white)}
  .intro__cta{position:absolute;left:12px;right:12px;top:533px;height:38px;font-size:12px}

  /* App header */
  .appbar{background:var(--white);border-bottom:1px solid var(--muted)}
  .appbar__row{height:38px;position:relative;display:flex;align-items:center;justify-content:center}
  .brand--bar{color:var(--accent);font-size:17px;font-weight:400}
  .brand--bar .brand__dot{width:8px;height:8px}
  .appbar__menu{position:absolute;right:12px;top:12px;width:18px;height:14px;display:flex;flex-direction:column;justify-content:space-between}
  .appbar__menu i{display:block;height:2px;background:#555}

  /* Feed */
  .search{margin:4px 4px 0;height:34px;border:2px solid var(--accent);display:flex;align-items:center;padding:0 8px;font-size:16px;color:var(--ink)}
  .feed{position:absolute;top:100px;left:0;right:0;bottom:0;display:flex;flex-direction:column;gap:4px}
  .card{flex:1;display:flex;align-items:center;justify-content:center;color:var(--white);font-size:12px;font-weight:600;text-shadow:0 1px 2px rgba(0,0,0,.5)}
  .card--one{background:linear-gradient(135deg,#9aa1aa,#6d737b)}
  .card--two{background:linear-gradient(180deg,#8fa4b6 0%,#57677a 55%,#3c4a58 100%)}
  .card--three{background:linear-gradient(135deg,#5a4b40,#2f2b2a)}

  /* Menu */
  .menu{position:absolute;top:62px;left:0;right:0;bottom:0;display:flex;flex-direction:column}
  .menu__item{flex:1;display:flex;align-items:center;border-bottom:1px solid var(--navy-line);color:var(--white)}
  .menu__item:last-child{border-bottom:none}
  .menu__icon{width:96px;display:flex;justify-content:center}
  .menu__label{flex:1;text-align:center;font-size:22px;line-height:1.3;padding-right:20px}
</style>
</head>
<body>
<main class="board">

  <!-- Sign up -->
  <section class="screen screen--signup">
    <div class="signup__photo" role="img" aria-label="Photo of a woman using her phone outdoors, darkened"></div>
    <div class="signup__content">
      <div class="status"><span class="status__signal"><i></i><i></i><i></i><i></i><i></i></span><span class="status__time">11:14 PM</span><span class="status__battery">100%<b></b></span></div>
      <div class="brand brand--hero">Bookora<span class="brand__dot"></span></div>
      <form class="form">
        <div class="field">Username</div>
        <div class="field">Mail</div>
        <div class="field">Password</div>
        <div class="btn btn--accent">Sign up</div>
        <div class="btn btn--connect">Sign up with Connectly</div>
        <p class="signin">Already registered?<strong>SIGN IN</strong></p>
      </form>
    </div>
  </section>

  <!-- Intro -->
  <section class="screen screen--intro">
    <div class="status"><span class="status__signal"><i></i><i></i><i></i><i></i><i></i></span><span class="status__time">11:14 PM</span><span class="status__battery">100%<b></b></span></div>
    <svg class="intro__orbit" viewBox="0 0 206 206" fill="none">
      <circle cx="103" cy="103" r="92" stroke="#f4b236" stroke-width="2" stroke-dasharray="6 5"/>
      <!-- plane -->
      <g fill="#fff" transform="translate(103 11)">
        <path d="M-2 -14 h4 v9 l14 7 v4 l-14 -4 v8 l4 3 v3 l-6 -2 l-6 2 v-3 l4 -3 v-8 l-14 4 v-4 l14 -7z"/>
      </g>
      <!-- person -->
      <g fill="#fff" transform="translate(195 103)">
        <circle cx="0" cy="-8" r="7"/>
        <path d="M-12 14 a12 12 0 0 1 24 0z"/>
      </g>
      <!-- tie -->
      <g transform="translate(103 195)" stroke="#fff" stroke-width="2" fill="#b455c9">
        <path d="M-5 -15 h10 l-2 5 l6 20 l-9 7 l-9 -7 l6 -20z"/>
        <path d="M-6 -2 l11 -4 M-6 6 l12 -4" />
      </g>
      <!-- document -->
      <g transform="translate(11 103)" stroke="#fff" stroke-width="2" fill="#b455c9">
        <path d="M-8 -16 h12 l6 6 v20 h-18z"/>
        <path d="M-4 -16 v-0 M-14 -10 h0" />
        <path d="M-4 -6 h9 M-4 -1 h9 M-4 4 h9"/>
      </g>
    </svg>
    <h2 class="intro__title">Search by</h2>
    <p class="intro__tag">We helps you stay organized</p>
    <div class="intro__dots"><i></i><i></i><i class="is-active"></i><i></i></div>
    <div class="btn btn--accent intro__cta">Get started</div>
  </section>

  <!-- Feed -->
  <section class="screen screen--feed">
    <header class="appbar">
      <div class="status status--dark"><span class="status__signal"><i></i><i></i><i></i><i></i><i></i></span><span class="status__time">11:14 PM</span><span class="status__battery">100%<b></b></span></div>
      <div class="appbar__row">
        <div class="brand brand--bar">Bookora<span class="brand__dot"></span></div>
        <div class="appbar__menu"><i></i><i></i><i></i></div>
      </div>
    </header>
    <div class="search">Type to search</div>
    <div class="feed">
      <div class="card card--one" role="img" aria-label="Photo of a person in a grey shirt">Pellentesque habitant morbi tristiqu</div>
      <div class="card card--two" role="img" aria-label="Aerial photo of a harbour city">Pellentesque habitant morbi tristiqu</div>
      <div class="card card--three" role="img" aria-label="Photo of a busy street market">Pellentesque habitant morbi tristiqu</div>
    </div>
  </section>

  <!-- Menu -->
  <section class="screen screen--menu">
    <header class="appbar">
      <div class="status status--dark"><span class="status__signal"><i></i><i></i><i></i><i></i><i></i></span><span class="status__time">11:14 PM</span><span class="status__battery">100%<b></b></span></div>
      <div class="appbar__row">
        <div class="brand brand--bar">Bookora<span class="brand__dot"></span></div>
        <div class="appbar__menu"><i></i><i></i><i></i></div>
      </div>
    </header>
    <nav class="menu">
      <div class="menu__item">
        <span class="menu__icon"><svg width="44" height="56" viewBox="0 0 44 56" fill="none" stroke="#fff" stroke-width="2.5"><circle cx="22" cy="15" r="11"/><path d="M4 54 v-10 a12 12 0 0 1 12 -12 h12 a12 12 0 0 1 12 12 v10z"/></svg></span>
        <span class="menu__label">Profile</span>
      </div>
      <div class="menu__item">
        <span class="menu__icon"><svg width="70" height="66" viewBox="0 0 70 66" fill="none" stroke="#fff" stroke-width="2.5"><path d="M4 64 h58"/><rect x="8" y="22" width="24" height="42"/><rect x="32" y="12" width="20" height="52"/><path d="M13 30h4M23 30h4M13 38h4M23 38h4M13 46h4M23 46h4M37 22h4M44 22h4M37 30h4M44 30h4M37 38h4M44 38h4"/><circle cx="56" cy="12" r="9" fill="#2c3d51"/><path d="M52 8l8 8M60 8l-8 8"/></svg></span>
        <span class="menu__label">Favourite<br>Companies</span>
      </div>
      <div class="menu__item">
        <span class="menu__icon"><svg width="70" height="66" viewBox="0 0 70 66" fill="none" stroke="#fff" stroke-width="2.5"><path d="M4 64 h58"/><rect x="8" y="22" width="24" height="42"/><rect x="32" y="12" width="20" height="52"/><path d="M13 30h4M23 30h4M13 38h4M23 38h4M13 46h4M23 46h4M37 30h4M44 30h4M37 38h4M44 38h4"/><circle cx="54" cy="14" r="9" fill="#2c3d51"/><path d="M60 21l7 7"/></svg></span>
        <span class="menu__label">Search<br>Companies</span>
      </div>
      <div class="menu__item">
        <span class="menu__icon"><svg width="66" height="62" viewBox="0 0 66 62" fill="none" stroke="#fff" stroke-width="2.5"><rect x="4" y="8" width="46" height="42" rx="3"/><path d="M4 18h46M14 3v10M40 3v10"/><path d="M11 26h5M21 26h5M31 26h5M11 34h5M21 34h5M11 42h5M21 42h5"/><circle cx="48" cy="44" r="15" fill="#2c3d51"/><path d="M48 35v9l6 4"/></svg></span>
        <span class="menu__label">Appointment</span>
      </div>
    </nav>
  </section>

</main>
</body>
</html>
```